Webdesign für einen  Bauträger und Projektentwickler
Webdesign für einen Bauträger und Projektentwickler
Zielgruppe
Wir sind ein Bauträger und Projektentwickler aus Ulm. Kapitalanleger sind hauptsächlich unsere Zielgruppe.
Aufgabenstellung
Die bereits bestehende Webseite soll überarbeitet werden bzw. das Design & Layout soll modernisiert werden. Das Design soll edel und klassisch sein. Die Webseite soll Menschen anziehen, die wertige Immobilien oder Bauprojekte suchen. Das Design sollte bevorzugt mit dem Tool Adobe Photoshop erstellt werden. Das Unternehmenslogo wurde kürzlich überarbeitet, wurde jedoch noch nicht gelauncht. Dies soll mit der überarbeiteten Webseite geschehen.

```html
<!DOCTYPE html>
<html lang="de">
<head>
<meta charset="utf-8">
<title>Holvert – Drei Höfe, Neu-Ulm</title>
<link href="https://fonts.googleapis.com/css2?family=Montserrat:wght@400;500&family=Questrial&family=Open+Sans:wght@400&display=swap" rel="stylesheet">
<style>
:root{
  --black:#000;
  --white:#fff;
  --yellow:#f7e100;
  --ink:#111;
  --veil:rgba(235,238,242,.62);
  --band:rgba(90,90,90,.45);
}
*{margin:0;padding:0;box-sizing:border-box}
html,body{width:688px;height:1200px;overflow:hidden;background:var(--white)}
body{position:relative;font-family:'Montserrat',sans-serif;color:var(--ink)}
.abs{position:absolute}

.site-header{left:0;top:0;width:688px;height:36px;background:var(--white)}
.brand{left:27px;top:8px;font-family:'Questrial',sans-serif;font-size:19px;letter-spacing:3px;color:var(--black);line-height:1}
.menu-toggle{left:626px;top:14px}

.hero{left:0;top:36px;width:688px;height:351px;background:linear-gradient(180deg,#7f9fcc 0%,#b9c6d6 30%,#c9c4bb 55%,#7e8a86 75%,#4f7a3a 100%)}
.hero-veil{left:0;top:158px;width:688px;height:94px;background:var(--veil)}
.hero-title{left:0;top:178px;width:688px;text-align:center;font-family:'Questrial',sans-serif;font-size:17px;letter-spacing:5px;color:var(--ink)}
.rule{height:2px;background:var(--yellow)}
.hero-rule{left:323px;top:205px;width:43px}
.hero-sub{left:0;top:219px;width:688px;text-align:center;font-family:'Questrial',sans-serif;font-size:13px;letter-spacing:5.2px;color:var(--ink)}
.btn-outline{left:302px;top:293px;width:83px;height:18px;border:1px solid #222;font-family:'Open Sans',sans-serif;font-size:6px;line-height:16px;text-align:center;color:#222}
.slider-arrow{top:194px;width:23px;height:23px;background:var(--yellow)}
.slider-arrow.prev{left:0}
.slider-arrow.next{left:665px}
.dots{left:481px;top:332px;display:flex;gap:2px}
.dots span{width:4px;height:4px;border-radius:50%;border:1px solid var(--yellow)}
.dots span.on{background:var(--yellow)}

.facts{left:0;top:387px;width:307px;height:231px;background:var(--black)}
.facts ul{list-style:none;position:absolute;left:76px;top:58px}
.facts li{position:relative;padding-left:12px;font-size:9px;line-height:20.7px;color:var(--white)}
.facts li::before{content:"";position:absolute;left:0;top:7px;width:6px;height:6px;border-radius:50%;background:var(--yellow)}
.description{left:364px;top:445px;width:296px;font-size:8.8px;line-height:10.4px;color:var(--ink)}
.description p+p{margin-top:10.4px}

.section-title{left:0;top:673px;width:688px;text-align:center;font-family:'Questrial',sans-serif;font-size:17px;letter-spacing:4px;color:var(--ink)}
.section-rule{left:322px;top:703px;width:43px}
.project-card{top:719px;height:240px}
.project-card .photo{position:absolute;inset:0}
.project-card .caption{position:absolute;left:0;right:0;top:102px;height:35px;background:var(--band);color:var(--white);font-family:'Open Sans',sans-serif;font-size:10px;line-height:13px;text-align:center;display:flex;align-items:center;justify-content:center}
.card-1{left:43px;width:197px}
.card-2{left:247px;width:196px}
.card-3{left:448px;width:196px}
.carousel-arrow{top:829px}
.btn-back{left:307px;top:989px;width:82px;height:18px;background:var(--yellow);font-family:'Open Sans',sans-serif;font-size:6px;line-height:18px;text-align:center;color:#222}

.site-footer{left:0;top:1044px;width:688px;height:156px;background:var(--black);color:var(--white)}
.footer-brand{position:absolute;left:20px;top:10px;font-family:'Questrial',sans-serif;font-size:30px;letter-spacing:5px;line-height:1}
.footer-col{position:absolute;top:66px;font-size:8.6px;line-height:12.9px}
.footer-address{left:21px}
.footer-nav{left:294px;width:100px;text-align:center}
.footer-legal{right:20px;text-align:right}
</style>
</head>
<body>

<header class="site-header abs">
  <div class="brand abs">HOLVERT</div>
  <svg class="menu-toggle abs" width="28" height="7" viewBox="0 0 28 7" aria-label="Menü">
    <rect x="0" y="0" width="28" height="1.2" fill="#000"/>
    <rect x="0" y="2.8" width="28" height="1.2" fill="#000"/>
    <rect x="0" y="5.6" width="28" height="1.2" fill="#000"/>
  </svg>
</header>

<section class="hero abs" role="img" aria-label="Foto: moderne Wohnanlage mit grauer Fassade, Bäumen und Gehweg unter blauem Himmel"></section>
<div class="hero-veil abs"></div>
<h1 class="hero-title abs">DREI HÖFE, NEU-ULM</h1>
<div class="rule hero-rule abs"></div>
<p class="hero-sub abs">24 WOHNEINHEITEN UND 4 PENTHÄUSER</p>
<div class="btn-outline abs">MEHR ERFAHREN</div>
<svg class="slider-arrow prev abs" viewBox="0 0 23 23" aria-label="Zurück">
  <polyline points="14,4 7,11.5 14,19" fill="none" stroke="#000" stroke-width="1.4"/>
</svg>
<svg class="slider-arrow next abs" viewBox="0 0 23 23" aria-label="Weiter">
  <polyline points="9,4 16,11.5 9,19" fill="none" stroke="#000" stroke-width="1.4"/>
</svg>
<div class="dots abs"><span class="on"></span><span></span><span></span><span></span><span></span></div>

<aside class="facts abs">
  <ul>
    <li>Baujahr: 2012</li>
    <li>24 Wohnheinheiten</li>
    <li>4 Penthäuser</li>
    <li>37 Tiefgaragenplätze</li>
    <li>barrierefreies Wohnen</li>
    <li>Zentral gelegen im Neu-Ulmer Lindenfeld-Areal</li>
  </ul>
</aside>
<div class="description abs">
  <p>Das Objekt Drei Höfe in Neu-Ulm besteht aus 24 Wohneinheiten, 4 Penthäusern und 37 Tiefgaragenstellplätzen. Der Standort überzeugt mit der guten Infrastuktur: öffentliche Verkehrsmittel, Schulen und Kindergärten, Einkaufszentrum und eine Arena für Sport- und Kulturveranstaltungen sind direkt vor der Tür oder in wenigen Gehminuten erreichbar.</p>
  <p>Auch Kapitalanleger sind zufrieden: "Die barrierefreie Wohnung in der Drei-Höfe-Anlage auf dem Neu-Ulmer Lindenfeld-Areal erfüllt beste Voraussetzungen für eine gute Vermietung, das Preis-Leistungsverhältnis stimmt."</p>
</div>

<h2 class="section-title abs">WEITERE ABGESCHLOSSENE PROJEKTE</h2>
<div class="rule section-rule abs"></div>

<svg class="carousel-arrow abs" style="left:18px" width="12" height="20" viewBox="0 0 12 20" aria-label="Zurück">
  <polyline points="10,2 2,10 10,18" fill="none" stroke="#000" stroke-width="1.3"/>
</svg>
<article class="project-card card-1 abs">
  <div class="photo" role="img" aria-label="Foto: sanierter Wohnblock mit beiger Fassade und Balkonen" style="background:linear-gradient(180deg,#c9cccf 0%,#d3cbb2 40%,#a9a593 80%,#8c8a82 100%)"></div>
  <div class="caption">ALBRECHT, ULM -<br>SANIERUNG BESTANDSGEBÄUDE</div>
</article>
<article class="project-card card-2 abs">
  <div class="photo" role="img" aria-label="Foto: Wohnhaus mit Balkonen und Spielplatz bei Sonne" style="background:linear-gradient(180deg,#3f7ad0 0%,#7ea6dc 30%,#6e6f6c 60%,#5f8a3c 80%,#bdbab2 100%)"></div>
  <div class="caption">SOLARA<br>GERSTHOFEN</div>
</article>
<article class="project-card card-3 abs">
  <div class="photo" role="img" aria-label="Foto: Gebäude mit roter Lamellenfassade vor blauem Himmel" style="background:linear-gradient(160deg,#4f7fc6 0%,#8c2f2f 35%,#9c3a3a 65%,#5a2424 100%)"></div>
  <div class="caption">GALERIEFORUM,<br>NEU ULM</div>
</article>
<svg class="carousel-arrow abs" style="left:659px" width="12" height="20" viewBox="0 0 12 20" aria-label="Weiter">
  <polyline points="2,2 10,10 2,18" fill="none" stroke="#000" stroke-width="1.3"/>
</svg>

<div class="btn-back abs">ZURÜCK</div>

<footer class="site-footer abs">
  <div class="footer-brand">HOLVERT</div>
  <div class="footer-col footer-address">
    Holvert Gruppe<br>Lindenweg 12<br>89073 Ulm<br><br>Tel: 0731 550240<br>info@brasimohr.de
  </div>
  <nav class="footer-col footer-nav">
    Projekte<br>Holvert Gruppe<br>Magazin<br>Aktuelles<br>Kontakt
  </nav>
  <div class="footer-col footer-legal">
    Datenschutz<br>Impressum
  </div>
</footer>

</body>
</html>
```